Crimson Harbor Quantive LLC

I am starting/launching my IT Consulting company in the Washington DC area. I just finished the logo design with PixelMeadow with the color palette in the attach. The mission and vision of the company is to help clients (mainly Federal Govt) "quantive" their business digital and business transformation journey . The name is intentional to incorporate my CH initials. I would like to have a PPT template for the company with a few different pages so it covers a text, table grids. I found a Veltronix PPT Sales Pitch template with new/modern design that Im attaching here as an example. I would like the pages content to model after this one, but the design can be what you come up with. I don't necessarily have to have a color accent line at top of the slide (it seems interfere with page real estate). The pictures will need to be more relevant to IT modernization, transformation, data/AI, digital workforce, consulting. The color team can be white background with light/darker gray, black, ivory and the 2 tones of teals in the logos be the accent. I would use the more muted teal more and the brighter teal to be stronger accent as needed. I found this website template color theme and look and feel to be quite fitting to what I envision
https://www.sitebramble.com/website-templates/professional-services
Thank you

```html
<!DOCTYPE html>
<html lang="en">
<head>
<meta charset="utf-8">
<title>Crimson Harbor Quantive – Slide Template</title>
<link href="https://fonts.googleapis.com/css2?family=Exo+2:wght@700;800&family=Noto+Sans:wght@400;600&display=swap" rel="stylesheet">
<style>
  :root{
    --page:#ecebec;
    --ink-dark:#05090b;
    --ink-deep:#0b1a20;
    --teal-bright:#13a8a3;
    --teal-muted:#2f7f80;
    --teal-slate:#244f5c;
    --logo-gray:#8fa4ad;
    --white:#ffffff;
    --text-dark:#1b1b1b;
    --panel:#1e2022;
  }
  *{box-sizing:border-box;margin:0;padding:0}
  html,body{width:1200px;height:1063px;overflow:hidden;background:var(--page)}
  body{position:relative;font-family:"Noto Sans",Arial,sans-serif}
  .slide{position:absolute;width:542px;height:305px;overflow:hidden;box-shadow:0 2px 5px rgba(0,0,0,.18)}
  .slide::after{content:"";position:absolute;left:0;right:0;bottom:0;height:4px;background:var(--teal-bright)}
  .slide--dark{background:var(--ink-dark)}
  .slide--light{background:var(--white)}
  .bg-visual{position:absolute;inset:0;background:
      radial-gradient(circle at 72% 30%,rgba(40,110,120,.45),transparent 45%),
      radial-gradient(circle at 20% 75%,rgba(30,80,95,.35),transparent 40%),
      radial-gradient(circle at 88% 80%,rgba(180,90,50,.18),transparent 30%),
      linear-gradient(135deg,#061015,#0c2129 55%,#04080a)}
  .title{font-family:"Exo 2",Arial,sans-serif;font-weight:800;letter-spacing:-.3px;position:absolute;white-space:nowrap}
  .title__mark{color:var(--teal-bright);margin-right:6px}
  .wordmark{font-family:"Noto Sans",Arial,sans-serif;font-weight:600;position:absolute;white-space:nowrap}

  /* cover */
  .cover__title{left:0;width:100%;text-align:center;top:131px;font-size:31px;color:var(--white)}
  .cover__band{position:absolute;left:0;bottom:0;width:330px;height:62px;background:linear-gradient(90deg,#111416,#1a1e21)}
  .cover__plate{position:absolute;left:0;top:0}
  .cover__wordmark{left:362px;top:258px;font-size:21px;color:var(--teal-slate);letter-spacing:.5px}

  /* about */
  .about__title{left:39px;top:30px;font-size:25px;color:var(--white)}
  .about__logo{position:absolute;left:368px;top:28px;width:152px;height:34px;background:#0c0f11;display:flex;align-items:center;justify-content:center}
  .about__logo .wordmark{position:static;font-size:18px;color:var(--logo-gray);letter-spacing:.5px}
  .about__panel{position:absolute;left:0;top:0}
  .about__text{position:absolute;left:190px;top:114px;width:345px;text-align:center;font-size:13.6px;line-height:20.4px;color:var(--text-dark)}

  /* small corner mark */
  .corner-mark{position:absolute;right:18px;top:14px;text-align:center}
  .corner-mark .wordmark{position:static;display:block;font-size:17px;line-height:18px}
  .corner-mark small{display:block;font-size:3px;letter-spacing:.2px}
  .corner-mark--light .wordmark{color:var(--teal-slate)}
  .corner-mark--light small{color:var(--teal-slate)}
  .corner-mark--dark .wordmark{color:var(--logo-gray)}
  .corner-mark--dark small{color:var(--logo-gray)}

  /* problem */
  .problem__title{left:18px;top:27px;font-size:26px;color:var(--teal-slate)}
  .problem__list{position:absolute;left:40px;top:81px;width:282px;list-style:none}
  .problem__list li{font-size:9.6px;line-height:12.2px;color:var(--text-dark);margin-bottom:12.4px}
  .problem__list b{color:var(--teal-bright);font-weight:600}
  .problem__image{position:absolute;left:346px;top:51px;width:196px;height:230px;border-radius:12px 0 0 12px;
      background:radial-gradient(circle at 50% 50%,#d98a52 0,#4fa4b0 22%,#9fc4d0 48%,#dce9ee 70%,#8aa3ad)}

  /* competition */
  .compete__title{left:18px;top:28px;font-size:26px;color:var(--white)}
  .compete__panel{position:absolute;top:73px;height:202px;border-radius:6px;background:rgba(40,42,44,.75)}
  .compete__panel--ours{left:20px;width:249px;border:1px solid var(--teal-muted)}
  .compete__panel--theirs{left:274px;width:248px;border:1px solid #5a5d60}
  .compete__rail{position:absolute;left:270px;top:95px;width:2px;height:160px;background:var(--teal-muted)}
  .compete__icon{position:absolute;left:249px;width:44px;height:44px;border-radius:50%;background:#000;border:1.5px solid var(--teal-bright);display:flex;align-items:center;justify-content:center}
  .compete__point{position:absolute;font-size:9.6px;line-height:12.2px;color:#e8e8e8}
  .compete__point--ours{left:40px;width:186px;text-align:right}
  .compete__point--theirs{left:314px;width:200px}

  /* market */
  .market__title{left:18px;top:28px;font-size:26px;color:var(--white)}
  .market__list{position:absolute;left:40px;top:113px;list-style:none;color:var(--white);font-size:13px;line-height:16.3px}
  .market__table{position:absolute;left:255px;top:104px;width:267px;border-collapse:separate;border-spacing:1px;background:transparent}
  .market__table th,.market__table td{width:53px;text-align:center;font-size:5.6px;color:var(--white)}
  .market__table th{height:25px;font-weight:600;background:rgba(20,22,24,.85)}
  .market__table td{height:25px;background:rgba(18,20,22,.9)}
  .market__table tr.is-accent td{background:var(--teal-muted)}
</style>
</head>
<body>

<!-- Cover -->
<section class="slide slide--dark" style="left:44px;top:44px">
  <div class="bg-visual" role="img" aria-label="Dark photo of a hand touching a glowing digital interface with teal bokeh lights"></div>
  <div class="cover__band"></div>
  <svg class="cover__plate" width="542" height="305" viewBox="0 0 542 305" aria-hidden="true">
    <polygon points="332,240 542,240 542,305 287,305" fill="#ffffff"/>
  </svg>
  <h1 class="title cover__title">PITCH DECK</h1>
  <span class="wordmark cover__wordmark">CHQUANTIVE</span>
</section>

<!-- About -->
<section class="slide slide--dark" style="left:615px;top:44px">
  <div class="bg-visual" role="img" aria-label="Dark photo of circuitry and glowing orange and teal light trails"></div>
  <h2 class="title about__title">ABOUT US</h2>
  <div class="about__logo"><span class="wordmark">CHQUANTIVE</span></div>
  <svg class="about__panel" width="542" height="305" viewBox="0 0 542 305" aria-hidden="true">
    <path d="M207,91 H542 V268 H207 Q197,268 191,259 L144,185 Q141,181 144,177 L191,100 Q197,91 207,91 Z" fill="#ffffff"/>
  </svg>
  <p class="about__text">At Norvale, we empower organizations to foster collaborative thinking to further drive workplace innovation. By closing the loop and leveraging agile frameworks, we help businesses grow organically and foster a consumer-first mindset.</p>
</section>

<!-- Problem -->
<section class="slide slide--light" style="left:329px;top:376px">
  <div class="corner-mark corner-mark--light"><span class="wordmark">CH</span><small>CRIMSON HARBOR QUANTIVE</small></div>
  <h2 class="title problem__title"><span class="title__mark">»</span>PROBLEM</h2>
  <ul class="problem__list">
    <li><b>Market gap:</b> few, if any, products on the market help customers like we do</li>
    <li><b>Customers:</b> 66% of US consumers spend money on multiple products that only partially resolves their issue</li>
    <li><b>Financials:</b> millennials account for about a quarter of the $48 billion spent on other products in 2018</li>
    <li><b>Costs:</b> loss of productivity costing consumers thousands of dollars</li>
    <li><b>Usability:</b> customers want something easy to use that helps make their life easier</li>
  </ul>
  <div class="problem__image" role="img" aria-label="Illustration of a hand holding a glowing transparent circuit device above clouds and a city"></div>
</section>

<!-- Competition -->
<section class="slide slide--dark" style="left:44px;top:707px">
  <div class="bg-visual" role="img" aria-label="Dark photo of a hand with a glowing teal digital interface"></div>
  <div class="corner-mark corner-mark--dark"><span class="wordmark">CH</span><small>CRIMSON HARBOR QUANTIVE</small></div>
  <h2 class="title compete__title"><span class="title__mark">»</span>OUR COMPETITION</h2>
  <div class="compete__panel compete__panel--ours"></div>
  <div class="compete__panel compete__panel--theirs"></div>
  <div class="compete__rail"></div>

  <div class="compete__icon" style="top:91px">
    <svg width="22" height="22" viewBox="0 0 24 24" fill="none" stroke="#fff" stroke-width="1.6" stroke-linejoin="round"><path d="M6 3h12v11l-6 7-6-7z"/><text x="12" y="14" font-size="9" text-anchor="middle" fill="#fff" stroke="none" font-family="Noto Sans,sans-serif" font-weight="600">$</text></svg>
  </div>
  <div class="compete__icon" style="top:154px">
    <svg width="22" height="22" viewBox="0 0 24 24" fill="none" stroke="#fff" stroke-width="1.6" stroke-linecap="round" stroke-linejoin="round"><path d="M8 21l-3-6 3-1 2 3V8a1.5 1.5 0 013 0v5l5 1-1 7z"/><path d="M11 2v2M6 4l1.5 1.5M16 4l-1.5 1.5"/></svg>
  </div>
  <div class="compete__icon" style="top:218px">
    <svg width="22" height="22" viewBox="0 0 24 24" fill="none" stroke="#fff" stroke-width="1.6" stroke-linecap="round" stroke-linejoin="round"><rect x="9" y="3" width="11" height="7" rx="1"/><circle cx="14.5" cy="6.5" r="1.5"/><path d="M3 14h5l4 2h5a1.5 1.5 0 010 3h-6M3 21h9l8-4"/></svg>
  </div>

  <p class="compete__point compete__point--ours" style="top:101px">Our product is priced below that of other companies on the market</p>
  <p class="compete__point compete__point--ours" style="top:152px">Design is simple and easy to use, compared to the complex designs of the competitors</p>
  <p class="compete__point compete__point--ours" style="top:217px">Affordability is the main draw for our consumers to our product</p>
  <p class="compete__point compete__point--theirs" style="top:107px">Company A product is more expensive</p>
  <p class="compete__point compete__point--theirs" style="top:158px">Companies B &amp; C product is expensive and inconvenient to use</p>
  <p class="compete__point compete__point--theirs" style="top:223px">Companies D &amp; E product is affordable, but inconvenient to use</p>
</section>

<!-- Market overview -->
<section class="slide slide--dark" style="left:615px;top:707px">
  <div class="bg-visual" role="img" aria-label="Dark photo of a hand with teal bokeh lights and digital particles"></div>
  <div class="corner-mark corner-mark--dark"><span class="wordmark">CH</span><small>CRIMSON HARBOR QUANTIVE</small></div>
  <h2 class="title market__title"><span class="title__mark">»</span>MARKET OVERVIEW</h2>
  <ul class="market__list">
    <li>Opportunity to build</li>
    <li>Fully inclusive market</li>
    <li>Total addressable market</li>
    <li>Freedom to invent</li>
    <li>Selectively inclusive market</li>
    <li>Serviceable available market</li>
  </ul>
  <table class="market__table">
    <tr><th></th><th>Clients</th><th>Order</th><th>Gross Revenue</th><th>Net Revenue</th></tr>
    <tr class="is-accent"><td>20XX</td><td>20XX</td><td>20XX</td><td>20XX</td><td>20XX</td></tr>
    <tr><td>20XX</td><td>20XX</td><td>20XX</td><td>20XX</td><td>20XX</td></tr>
    <tr class="is-accent"><td>20XX</td><td>20XX</td><td>20XX</td><td>20XX</td><td>20XX</td></tr>
    <tr><td>20XX</td><td>20XX</td><td>20XX</td><td>20XX</td><td>20XX</td></tr>
  </table>
</section>

</body>
</html>
```